District Manager Business Card

Hello, I own 3 automotive repair shops that are all 3 different names. I need a card that has all 3 locations and logos on it. Just a simple, modern, clean design. I selected double sided, but If a single side is more ideal, thats ok too. I am open to explore both options. I attached the 3 logos in a few different formats.

Industry/Entity Type

Auto Repair

Contact Information for Business Card

Requirements
Must have
• Location information:
Q&L Automotive
482 Birchfield Ave.
Crossville TN 38555

MOTO MEND
257 Pine Hollow Turnpike
Oak Ridge TN 37830

Brantmoor Tire & Auto
614 North Aspen Ave.
Cookeville TN 38501

District Manager - Dale Hobart - Dale@qandlauto-example.com - Cell: 931-555-0196
Nice to have
• This can be a single or a double sided card. Just want a clean card that shows all 3 locations.

```html
<!DOCTYPE html>
<html lang="en">
<head>
<meta charset="utf-8">
<title>Dale Hobart – District Manager</title>
<link rel="stylesheet" href="https://fonts.googleapis.com/css2?family=Montserrat:wght@300;400;600;700&display=swap">
<style>
  :root {
    --navy: #0e223b;
    --panel: #dce0e3;
    --amber: #fea500;
    --rust: #c46c06;
    --ink: #2b2b30;
    --text: #1c1c20;
    --muted: #4a4d55;
  }
  * { margin: 0; padding: 0; box-sizing: border-box; }
  html, body {
    width: 1200px;
    height: 720px;
    overflow: hidden;
    background: var(--navy);
  }
  .card {
    position: relative;
    width: 1200px;
    height: 720px;
    overflow: hidden;
    background: var(--navy);
    font-family: "Montserrat", sans-serif;
  }
  .card-shapes {
    position: absolute;
    inset: 0;
    width: 1200px;
    height: 720px;
  }

  /* Name and role */
  .identity {
    position: absolute;
    right: 97px;
    top: 200px;
    text-align: right;
  }
  .identity-name {
    font-weight: 700;
    font-size: 50px;
    line-height: 1;
    letter-spacing: 0.5px;
    color: var(--ink);
  }
  .identity-name .surname {
    color: var(--amber);
    margin-left: 18px;
  }
  .identity-role {
    margin-top: 8px;
    font-weight: 300;
    font-size: 31px;
    line-height: 1;
    color: var(--text);
  }

  /* Contact rows */
  .contact-list {
    position: absolute;
    right: 101px;
    top: 328px;
    list-style: none;
    display: flex;
    flex-direction: column;
    align-items: flex-end;
    gap: 14px;
  }
  .contact-item {
    display: flex;
    align-items: center;
    gap: 30px;
    font-weight: 400;
    font-size: 21px;
    line-height: 1;
    color: var(--text);
  }
  .contact-icon {
    width: 44px;
    height: 44px;
    flex: none;
  }

  /* Shop locations */
  .locations {
    position: absolute;
    left: 26px;
    top: 322px;
    display: flex;
    gap: 14px;
    list-style: none;
  }
  .location {
    width: 186px;
    color: var(--muted);
    font-size: 12px;
    line-height: 1.45;
    font-weight: 400;
  }
  .location-brand {
    display: flex;
    align-items: center;
    gap: 6px;
    margin-bottom: 4px;
    font-weight: 700;
    font-size: 13px;
    line-height: 1.2;
    color: var(--ink);
    white-space: nowrap;
  }
  .location-mark {
    width: 10px;
    height: 10px;
    border-radius: 50%;
    background: var(--amber);
    flex: none;
  }
  .location address {
    font-style: normal;
  }
</style>
</head>
<body>
  <main class="card">
    <svg class="card-shapes" viewBox="0 0 1125 675" width="1200" height="720" aria-hidden="true">
      <polygon class="panel" fill="var(--panel)"
        points="0,276 284,276 332,196 427,196 455,153 530,153 552,117 610,117 634,76 982,76 1125,232 1125,440 982,598 634,598 610,558 552,558 530,521 455,521 427,479 332,479 284,398 0,398"/>
      <polygon class="stripe-amber" fill="var(--amber)" points="448,0 545,0 427,196 332,196"/>
      <polygon class="stripe-rust" fill="var(--rust)" points="545,0 622,0 530,153 455,153"/>
      <polygon class="stripe-amber" fill="var(--amber)" points="332,479 427,479 545,675 448,675"/>
      <polygon class="stripe-rust" fill="var(--rust)" points="455,521 530,521 622,675 545,675"/>
    </svg>

    <header class="identity">
      <h1 class="identity-name">DALE<span class="surname">HOBART</span></h1>
      <p class="identity-role">DISTRICT MANAGER</p>
    </header>

    <ul class="contact-list">
      <li class="contact-item contact-email">
        <span>Dale@qandlauto-example.com</span>
        <svg class="contact-icon" viewBox="0 0 44 44" aria-hidden="true">
          <circle cx="22" cy="22" r="22" fill="var(--navy)"/>
          <rect x="10" y="13" width="24" height="18" fill="var(--amber)"/>
          <polyline points="10,13 22,23 34,13" fill="none" stroke="var(--navy)" stroke-width="1.6"/>
          <line x1="10" y1="31" x2="19" y2="21" stroke="var(--navy)" stroke-width="1.2"/>
          <line x1="34" y1="31" x2="25" y2="21" stroke="var(--navy)" stroke-width="1.2"/>
        </svg>
      </li>
      <li class="contact-item contact-web">
        <span>www.qandlauto-example.com</span>
        <svg class="contact-icon" viewBox="0 0 44 44" aria-hidden="true">
          <circle cx="22" cy="22" r="22" fill="var(--navy)"/>
          <g fill="none" stroke="var(--amber)" stroke-width="1.8">
            <circle cx="22" cy="22" r="11"/>
            <ellipse cx="22" cy="22" rx="5" ry="11"/>
            <line x1="11" y1="22" x2="33" y2="22"/>
          </g>
        </svg>
      </li>
      <li class="contact-item contact-phone">
        <span>Cell: 931 555 0196</span>
        <svg class="contact-icon" viewBox="0 0 44 44" aria-hidden="true">
          <circle cx="22" cy="22" r="22" fill="var(--navy)"/>
          <path d="M9,17 q13,-10 26,0 l0,4 l-6,0 l0,-3 q-7,-3 -14,0 l0,3 l-6,0 z" fill="var(--amber)"/>
          <path d="M13,21 l4,-2 l10,0 l4,2 l2,11 l-22,0 z" fill="var(--amber)"/>
          <circle cx="22" cy="26" r="3.4" fill="var(--navy)"/>
          <circle cx="22" cy="26" r="1.4" fill="var(--amber)"/>
        </svg>
      </li>
    </ul>

    <ul class="locations">
      <li class="location">
        <p class="location-brand"><span class="location-mark"></span>Q&amp;L Automotive</p>
        <address>482 Birchfield Ave.<br>Crossville TN 38555</address>
      </li>
      <li class="location">
        <p class="location-brand"><span class="location-mark"></span>MOTO MEND</p>
        <address>257 Pine Hollow Turnpike<br>Oak Ridge TN 37830</address>
      </li>
      <li class="location">
        <p class="location-brand"><span class="location-mark"></span>Brantmoor Tire &amp; Auto</p>
        <address>614 North Aspen Ave.<br>Cookeville TN 38501</address>
      </li>
    </ul>
  </main>
</body>
</html>
```